Business Card Design Project

Design is for the business card of a holistic, integral therapist. Design is required for front (colour / pattern) and back (white, with text as below).

Please prepare the design using placeholder text. I will work with the winning submission to complete the final information in the last iteration.

To give you a sense of her services a profile is below:
- I offer an integrative approach for effective relief of many issues such as anxiety, panic attacks, relationship difficulties, and health problems. In my counselling sessions I mainly use EFT {Emotional Freedom Technique } which taps into the body's energy system (meridians) to clear up blockages and limiting /distorted thinking and beliefs. I also work on expanding awareness as well as enhancing relationships.Clients have found the sessions life changing and report feeling lighter, clearer more empowered and connected to themselves and others.

Target Market(s)

Well educated, upper socioeconomic people seeking purpose and happiness in their lives.

Industry/Entity Type

Health

Requirements
Must have
• Must have the following text on front

First Name, Last Name
LLB, ND, Dip C
Counselling & Naturopathy
Emotional Feedom Technique and Bowen Therapy

Adress 1 Line 1
Adress 1 Line 2

Adress 2 Line 1
Adress 2 Line 2

xxx.xxx@xxxxx.com

Tel: 0XXX XXX XXX

Must have the following text on reverse - which should be primarily white.

Next appointment
Date:
Time:
Nice to have
• Example colour palettes

http://www.huepinwheel.net/palette/512093/velvet_lantern
http://www.huepinwheel.net/palette/308215/Quiet_Orchard
http://www.huepinwheel.net/palette/426958/Soft_Harbor_Glow

Example images that may be useful...
http://www.brindlemart.net/gp/product/images/4719260351/ref=dp_image_text_0?ie=UTF8&n=617204&s=books
http://www.brindlemart.net/gp/customer-media/product-gallery/5280147936/ref=cm_ciu_pdp_images_all
http://en.lorewell.org/wiki/File:Lotus_Grid_256bw.gif

```html
<!DOCTYPE html>
<html lang="en">
<head>
<meta charset="utf-8">
<title>Holistic Therapist Business Card – Front and Reverse</title>
<link rel="stylesheet" href="https://fonts.googleapis.com/css2?family=Didact+Gothic&display=swap">
<style>
  :root {
    --page-bg: #ffffff;
    --card-orange: #de8026;
    --card-text-light: #fff6ea;
    --reverse-bg: #ffffff;
    --reverse-border: #8a8a8a;
    --reverse-text: #222222;
    --pattern-soft: #f1f1f1;
    --pattern-line: #cfcfcf;
  }

  * { box-sizing: border-box; margin: 0; padding: 0; }

  html, body {
    width: 1200px;
    height: 900px;
    overflow: hidden;
    background: var(--page-bg);
  }

  body {
    position: relative;
    font-family: "Didact Gothic", "Century Gothic", sans-serif;
  }

  .card {
    position: absolute;
    width: 628px;
    height: 350px;
    overflow: hidden;
  }

  /* Front */
  .card--front {
    left: 104px;
    top: 77px;
    background: var(--card-orange);
  }

  .card__mandala {
    position: absolute;
    left: 0;
    top: 0;
    width: 628px;
    height: 350px;
  }

  .contact {
    position: absolute;
    right: 21px;
    top: 15px;
    text-align: right;
    color: var(--card-text-light);
    font-size: 15.5px;
    line-height: 21px;
    letter-spacing: 0.1px;
  }

  .contact__group + .contact__group { margin-top: 21px; }

  /* Reverse */
  .card--reverse {
    left: 484px;
    top: 471px;
    background: var(--reverse-bg);
    border: 1.5px solid var(--reverse-border);
  }

  .card__lineart {
    position: absolute;
    left: 0;
    top: 0;
    width: 628px;
    height: 350px;
  }

  .appointment {
    position: absolute;
    left: 20px;
    top: 14px;
    color: var(--reverse-text);
    font-size: 19.5px;
  }

  .appointment__title { line-height: 26px; }
  .appointment__field { line-height: 26px; }
  .appointment__field--date { margin-top: 28px; }
  .appointment__field--time { margin-top: 82px; }
</style>
</head>
<body>

  <section class="card card--front" aria-label="Business card front">
    <svg class="card__mandala" viewBox="0 0 628 350" role="img"
         aria-label="Colourful floral mandala ornament in orange, red, purple, cream and green, half visible on the left edge">
      <defs>
        <radialGradient id="mandalaTones" cx="46" cy="173" r="320" gradientUnits="userSpaceOnUse">
          <stop offset="0" stop-color="#e58a2a"/>
          <stop offset="0.35" stop-color="#d9603a"/>
          <stop offset="0.6" stop-color="#c9583f"/>
          <stop offset="0.8" stop-color="#e3a04a"/>
          <stop offset="0.9" stop-color="#f1dfa8"/>
          <stop offset="0.96" stop-color="#2f8a5a"/>
          <stop offset="1" stop-color="#f3e6b6"/>
        </radialGradient>
      </defs>
      <path d="M0 0 H315 A320 320 0 0 1 315 350 H0 Z" fill="url(#mandalaTones)"/>
    </svg>

    <div class="contact">
      <p class="contact__group">
        First Name, Last Name<br>
        LLB, ND, Dip C<br>
        Counselling &amp; Naturopathy<br>
        Emotional Feedom Technique<br>
        and Bowen Therapy
      </p>
      <p class="contact__group">
        Adress 1 Line 1<br>
        Adress 1 Line 2
      </p>
      <p class="contact__group">
        Adress 2 Line 1<br>
        Adress 2 Line 2
      </p>
      <p class="contact__group">xxx.xxx@xxxxx.com</p>
      <p class="contact__group">Tel: 0XXX XXX XXX</p>
    </div>
  </section>

  <section class="card card--reverse" aria-label="Business card reverse">
    <svg class="card__lineart" viewBox="0 0 628 350" role="img"
         aria-label="Faint grey line-art floral mandala ornament, half visible on the right edge">
      <path d="M332 0 H628 V350 H321 A330 330 0 0 1 332 0 Z"
            fill="var(--pattern-soft)" stroke="var(--pattern-line)" stroke-width="1"/>
    </svg>

    <div class="appointment">
      <p class="appointment__title">Next appointment</p>
      <p class="appointment__field appointment__field--date">Date:</p>
      <p class="appointment__field appointment__field--time">Time:</p>
    </div>
  </section>

</body>
</html>
```